Business Card Design Project - IT Company

CLOUD IT company working with medium to large corporate clients requires 2 sided Business Card design.

Strong, Professional and modern is what I am looking for.

The Logo JPG attached has all the colour palette options. which consist of Red and Silver on various backgrounds

Preferred option for the Back of card is either Silver Text on Red or Silver Text on Black. Though this is not concrete. Surprise me.

Logo must be prominent along with Contact details of the staff member

Tagline can be all Capitals " CLOUD MANAGED SERVICES"

I will look to provide feedback and tweaks to get the right design so it should be a fun process.

I will provide the layered files to the top few contenders.

Reason: Leaving the door open for some creativity. Don't forget this is an technology company. .

Target Market(s)

Leaders, decision makers, CEOs, CIOs,

Industry/Entity Type

Business

Requirements
Must have
• Data must have is

Company Name: Brelquist
Tagline: Cloud Managed Services

No Particular order

First Name Last name
Director
Mobile 0477 555 019
www.brelquist-example.com
First.Lastname@brelquist-example.com
Suite 7, 48 Wexmoor Lane, Sydney NSW 2000

```html
<!DOCTYPE html>
<html lang="en">
<head>
<meta charset="utf-8">
<title>Brelquist – Business Card</title>
<link href="https://fonts.googleapis.com/css2?family=Exo+2:wght@400;500;600;700&display=swap" rel="stylesheet">
<style>
  :root {
    --canvas: #e6e6e6;
    --card-white: #fbfbfa;
    --ink: #2b2b2b;
    --ink-soft: #3d3d3d;
    --red: #b5141e;
    --red-deep: #8e0f16;
    --silver: #d3d5d8;
    --silver-soft: #b9bcc0;
  }
  * { box-sizing: border-box; margin: 0; padding: 0; }
  html, body {
    width: 1200px; height: 800px; overflow: hidden;
    background: var(--canvas);
    font-family: "Exo 2", sans-serif;
  }
  .stage {
    width: 1200px; height: 800px;
    display: flex; align-items: center; justify-content: center; gap: 40px;
  }
  .card {
    position: relative;
    width: 520px; height: 297px;
    box-shadow: 0 6px 18px rgba(0,0,0,.18);
    overflow: hidden;
  }

  /* Front */
  .card--front { background: var(--card-white); color: var(--ink); }
  .brand {
    position: absolute; left: 38px; top: 62px;
    display: flex; align-items: center; gap: 12px;
  }
  .brand__dot {
    width: 30px; height: 30px; border-radius: 50%;
    background: var(--red);
  }
  .brand__name {
    font-size: 44px; font-weight: 700; line-height: 1; letter-spacing: -0.5px;
    color: var(--ink);
  }
  .brand__tagline {
    position: absolute; left: 80px; top: 108px;
    font-size: 10.5px; font-weight: 600; letter-spacing: .4px;
    color: var(--ink);
  }
  .company-details {
    position: absolute; right: 270px; top: 150px;
    text-align: right; font-size: 13px; line-height: 1.3; color: var(--ink-soft);
  }
  .company-details__web { margin-bottom: 22px; }
  .company-details__web span { color: var(--red); font-weight: 600; }
  .person {
    position: absolute; left: 272px; top: 118px;
    color: var(--ink);
  }
  .person__name { font-size: 19px; font-weight: 600; letter-spacing: .3px; }
  .person__role { font-size: 13px; color: var(--ink-soft); margin-top: 2px; }
  .person__contacts { list-style: none; margin-top: 22px; font-size: 11.5px; color: var(--ink-soft); }
  .person__contacts li { display: flex; align-items: center; gap: 7px; margin-bottom: 4px; }
  .person__contacts svg { flex: none; }
  .front-band { position: absolute; left: 0; bottom: 0; }

  /* Back */
  .card--back {
    background: linear-gradient(160deg, var(--red) 0%, var(--red-deep) 100%);
    color: var(--silver);
  }
  .back-brand {
    position: absolute; left: 0; right: 0; top: 100px;
    display: flex; flex-direction: column; align-items: center;
  }
  .back-brand__row { display: flex; align-items: center; gap: 14px; }
  .back-brand__dot {
    width: 36px; height: 36px; border-radius: 50%;
    background: var(--silver);
  }
  .back-brand__name { font-size: 54px; font-weight: 700; line-height: 1; color: var(--silver); }
  .back-brand__tagline {
    margin-top: 6px; margin-left: 50px;
    font-size: 12.5px; font-weight: 600; letter-spacing: .6px; color: var(--silver-soft);
  }
  .back-web {
    position: absolute; right: 26px; bottom: 20px;
    font-size: 12px; color: var(--silver-soft);
  }
</style>
</head>
<body>
<main class="stage">

  <section class="card card--front" aria-label="Business card front">
    <div class="brand">
      <span class="brand__dot"></span>
      <span class="brand__name">Brelquist</span>
    </div>
    <p class="brand__tagline">CLOUD MANAGED SERVICES</p>

    <div class="company-details">
      <p class="company-details__web">www.<span>brelquist</span>-example.com</p>
      <p>Suite 7, 48 Wexmoor Lane</p>
      <p>Sydney NSW 2000</p>
    </div>

    <div class="person">
      <p class="person__name">MARLO FENWICK</p>
      <p class="person__role">Director</p>
      <ul class="person__contacts">
        <li>
          <svg width="9" height="13" viewBox="0 0 9 13" aria-hidden="true">
            <rect x="0.75" y="0.75" width="7.5" height="11.5" rx="1.5" fill="none" stroke="#b5141e" stroke-width="1.5"/>
            <circle cx="4.5" cy="10" r="0.9" fill="#b5141e"/>
          </svg>
          0477 555 019
        </li>
        <li>
          <svg width="12" height="9" viewBox="0 0 12 9" aria-hidden="true">
            <rect width="12" height="9" fill="#b5141e"/>
            <path d="M0.5 0.8 L6 5 L11.5 0.8" fill="none" stroke="#fbfbfa" stroke-width="1"/>
          </svg>
          marlo.fenwick@brelquist-example.com
        </li>
      </ul>
    </div>

    <svg class="front-band" width="520" height="24" viewBox="0 0 520 24" aria-hidden="true">
      <polygon points="236,0 520,0 520,24 228,24" fill="#b5141e"/>
    </svg>
  </section>

  <section class="card card--back" aria-label="Business card back">
    <div class="back-brand">
      <div class="back-brand__row">
        <span class="back-brand__dot"></span>
        <span class="back-brand__name">Brelquist</span>
      </div>
      <p class="back-brand__tagline">CLOUD MANAGED SERVICES</p>
    </div>
    <p class="back-web">www.brelquist-example.com</p>
  </section>

</main>
</body>
</html>
```